Toy company needs a banner design

I need a banner design to go on my Facebook and website home page. I already have a logo, the banner needs to be in some kinds of relation to my logo, or just photos to match my products. We manufacture and wholesale stuffed animals, the customization is the key feature. Sewn by Giants is our company name and we are trying to give the message of our unique designed and high quality products, environmental friendly materials and customization on almost every piece.

Target Market(s)

Corporate gifts, individual gifts (birthday, anniversary, graduation, wedding)

Industry/Entity Type

Toy Store

Logo Text

Green Cuddle Pals

Number of Pages Required

5+ page

Logo styles of interest
Abstract Logo
Font styles to use
Decorative

Requirements
Nice to have
• toy pictures or drawings

```html
<!DOCTYPE html>
<html lang="en">
<head>
<meta charset="utf-8">
<title>Sewn by Giants – Banners</title>
<link rel="stylesheet" href="https://fonts.googleapis.com/css2?family=Gochi+Hand&display=swap">
<style>
  :root {
    --stage: #2f2f2f;
    --paper: #ffffff;
    --brand-red: #e0473a;
    --brand-blue: #4db3d8;
    --brand-yellow: #f2bb2a;
    --ink: #3a3a3a;
  }
  * { margin: 0; padding: 0; box-sizing: border-box; }
  html, body { width: 1200px; height: 1000px; overflow: hidden; background: var(--stage); }
  .canvas { position: relative; width: 1200px; height: 1000px; background: var(--stage); }
  .banner { position: absolute; left: 167px; width: 851px; height: 314px; background: var(--paper); overflow: hidden; }
  .banner--intro { top: 114px; }
  .banner--values { top: 543px; }

  .toy { position: absolute; border-radius: 50%; }

  .brand { position: absolute; display: flex; flex-direction: column; align-items: center; gap: 8px; }
  .brand-dot { width: 62px; height: 62px; border-radius: 50%; background: var(--brand-red); }
  .brand-name { font-family: "Gochi Hand", cursive; font-size: 22px; line-height: 1; color: var(--brand-blue); white-space: nowrap; }

  .tagline { position: absolute; left: 0; width: 851px; text-align: center; font-family: "Gochi Hand", cursive; line-height: 1; white-space: nowrap; }
  .tagline--services { top: 185px; font-size: 28px; letter-spacing: 1px; }
  .tagline--product { top: 232px; font-size: 38px; letter-spacing: 2px; color: var(--brand-yellow); }
  .blue { color: var(--brand-blue); }
  .red { color: var(--brand-red); }
  .ink { color: var(--ink); }

  .value { position: absolute; font-family: "Gochi Hand", cursive; font-size: 27px; line-height: 1; letter-spacing: 2px; white-space: nowrap; }
  .value--design { left: 145px; top: 199px; color: var(--brand-red); }
  .value--quality { left: 83px; top: 242px; color: var(--brand-blue); }

  .puppets { position: absolute; left: 453px; top: 0; width: 398px; height: 314px;
    background:
      radial-gradient(ellipse 60px 70px at 75px 135px, rgba(240,225,232,.95), transparent),
      radial-gradient(ellipse 55px 55px at 130px 85px, rgba(110,180,220,.9), transparent),
      radial-gradient(ellipse 55px 60px at 200px 60px, rgba(240,170,200,.9), transparent),
      radial-gradient(ellipse 55px 55px at 275px 105px, rgba(120,190,80,.85), transparent),
      radial-gradient(ellipse 55px 55px at 300px 160px, rgba(245,220,80,.9), transparent),
      radial-gradient(ellipse 50px 55px at 40px 245px, rgba(140,140,140,.85), transparent),
      radial-gradient(ellipse 45px 55px at 110px 225px, rgba(225,200,160,.9), transparent),
      radial-gradient(ellipse 45px 55px at 190px 215px, rgba(90,90,90,.7), transparent),
      radial-gradient(ellipse 45px 50px at 250px 240px, rgba(200,140,70,.85), transparent),
      radial-gradient(ellipse 55px 50px at 320px 260px, rgba(235,235,235,.95), transparent),
      radial-gradient(ellipse 160px 110px at 170px 260px, rgba(214,170,150,.8), transparent),
      #f8f6f4; }
</style>
</head>
<body>
<main class="canvas">
  <section class="banner banner--intro">
    <div class="toy" role="img" aria-label="Plush penguin toy" style="left:14px;top:42px;width:134px;height:156px;transform:rotate(-18deg);background:radial-gradient(ellipse at 50% 50%,#8d8d8d 0%,#5a5a5a 45%,rgba(242,169,59,.85) 68%,rgba(255,255,255,0) 72%);"></div>
    <div class="toy" role="img" aria-label="Plush unicorn toy" style="left:172px;top:26px;width:72px;height:116px;background:radial-gradient(ellipse at 50% 50%,#d94f96 0%,#4aa9d8 50%,rgba(255,255,255,0) 71%);"></div>
    <div class="toy" role="img" aria-label="Plush teddy bear toy" style="left:90px;top:186px;width:94px;height:92px;background:radial-gradient(circle,#c98a45 0%,#9a6630 55%,rgba(255,255,255,0) 71%);"></div>
    <div class="brand" style="left:353px;top:14px;width:140px;">
      <span class="brand-dot"></span>
      <span class="brand-name">Sewn by Giants</span>
    </div>
    <p class="tagline tagline--services"><span class="blue">MANUFACTURE</span> <span class="ink">and</span> <span class="red">WHOLESALE</span></p>
    <p class="tagline tagline--product">STUFFED ANIMALS</p>
    <div class="toy" role="img" aria-label="Plush green turtle toy" style="left:586px;top:38px;width:88px;height:96px;background:radial-gradient(circle,#8cc65a 0%,#4e8e34 55%,rgba(255,255,255,0) 71%);"></div>
    <div class="toy" role="img" aria-label="Plush reindeer toy" style="left:696px;top:42px;width:154px;height:148px;transform:rotate(-15deg);background:radial-gradient(ellipse,#f4efe8 0%,#e8ddd0 22%,#a0703f 45%,#6e4526 60%,rgba(255,255,255,0) 71%);"></div>
    <div class="toy" role="img" aria-label="Small plush toy in a patterned egg" style="left:670px;top:214px;width:72px;height:76px;background:radial-gradient(circle,#f4d23a 0%,#8c5ab8 40%,#f08a3a 58%,rgba(255,255,255,0) 71%);"></div>
  </section>

  <section class="banner banner--values">
    <div class="brand" style="left:181px;top:28px;width:140px;">
      <span class="brand-dot"></span>
      <span class="brand-name">Sewn by Giants</span>
    </div>
    <p class="value value--design">UNIQUE DESIGN</p>
    <p class="value value--quality">HIGH QUALITY PRODUCT</p>
    <div class="puppets" role="img" aria-label="Photo of colourful plush animal finger puppets on a hand"></div>
  </section>
</main>
</body>
</html>
```